Residential Remodeling Contractor needs updated business card

I need a new design for my business card.
Name of the company is Brookfell Construction. I need a card that commands presence, strength, integrity. I have been in business for 28 years. I am a Residential Remodeling Contractor that covers all aspects of a residential remodel and build.

```html
<!DOCTYPE html>
<html lang="en">
<head>
<meta charset="utf-8">
<title>Brookfell Construction — Business Card</title>
<link rel="stylesheet" href="https://fonts.googleapis.com/css2?family=Cormorant+SC:wght@700&family=Montserrat:wght@300;400;700&display=swap">
<style>
  :root {
    --stage: #ececec;
    --navy: #203d7c;
    --paper: #ffffff;
    --ink-grey: #6f6f6f;
    --rule: #cfcfcf;
    --white: #ffffff;
  }
  * { margin: 0; padding: 0; box-sizing: border-box; }
  html, body {
    width: 1200px;
    height: 1200px;
    overflow: hidden;
    background: var(--stage);
  }
  .canvas {
    position: relative;
    width: 1200px;
    height: 1200px;
  }
  .card {
    position: absolute;
    left: 226px;
    width: 746px;
    height: 436px;
    border-radius: 25px;
    overflow: hidden;
  }
  .card-front {
    top: 130px;
    background: var(--navy);
  }
  .card-back {
    top: 639px;
    background: var(--paper);
  }
  .brand-name {
    font-family: "Cormorant SC", "Times New Roman", serif;
    font-weight: 700;
    line-height: 1;
    text-transform: uppercase;
  }
  .front-brand {
    position: absolute;
    right: 64px;
    top: 240px;
    text-align: right;
    color: var(--white);
    font-size: 44px;
    letter-spacing: 1px;
  }
  .front-brand span { display: block; }
  .front-brand span + span { margin-top: 4px; }
  .back-brand {
    position: absolute;
    left: 304px;
    left: 52px;
    top: 74px;
    color: var(--navy);
    font-size: 22px;
    letter-spacing: 0.5px;
  }
  .back-brand span { display: block; }
  .person {
    position: absolute;
    left: 46px;
    top: 241px;
    font-family: "Montserrat", Arial, sans-serif;
  }
  .person-name {
    color: var(--navy);
    font-weight: 700;
    font-size: 19px;
    letter-spacing: 3.5px;
  }
  .person-role {
    margin-top: 6px;
    color: var(--navy);
    font-weight: 300;
    font-size: 18px;
    letter-spacing: 3px;
  }
  .divider {
    position: absolute;
    left: 46px;
    right: 36px;
    top: 302px;
    height: 1px;
    background: var(--rule);
  }
  .contacts {
    position: absolute;
    left: 46px;
    top: 320px;
    list-style: none;
    font-family: "Montserrat", Arial, sans-serif;
    font-size: 19px;
    color: var(--ink-grey);
  }
  .contacts li {
    display: flex;
    align-items: center;
    height: 29.5px;
  }
  .contacts svg {
    width: 18px;
    height: 18px;
    margin-right: 16px;
    fill: var(--navy);
    flex: none;
  }
</style>
</head>
<body>
<main class="canvas">
  <section class="card card-front" aria-label="Business card front">
    <h1 class="brand-name front-brand"><span>Brookfell</span><span>Construction</span></h1>
  </section>

  <section class="card card-back" aria-label="Business card back">
    <p class="brand-name back-brand"><span>Brookfell</span><span>Construction</span></p>

    <div class="person">
      <p class="person-name">NAME SURNAME</p>
      <p class="person-role">Position</p>
    </div>

    <div class="divider"></div>

    <ul class="contacts">
      <li>
        <svg viewBox="0 0 18 18" aria-hidden="true"><path d="M5 1h8a1.5 1.5 0 0 1 1.5 1.5v13A1.5 1.5 0 0 1 13 17H5a1.5 1.5 0 0 1-1.5-1.5v-13A1.5 1.5 0 0 1 5 1zm.5 2v10h7V3zm3.5 11.2a1 1 0 1 0 0 2 1 1 0 0 0 0-2z"/></svg>
        123-456-7890
      </li>
      <li>
        <svg viewBox="0 0 18 18" aria-hidden="true"><path d="M1 4h16v10H1zm1.6 1.2L9 10l6.4-4.8zM2.2 6.6v6.2h13.6V6.6L9 11.6z"/></svg>
        email@website.com
      </li>
      <li>
        <svg viewBox="0 0 18 18" aria-hidden="true"><path d="M9 1.5a7.5 7.5 0 1 0 0 15 7.5 7.5 0 0 0 0-15zm-.7 1.6v2.6H6.2C6.7 4.3 7.4 3.3 8.3 3.1zm1.4 0c.9.2 1.6 1.2 2.1 2.6H9.7zM5 3.9c-.2.5-.4 1.1-.5 1.8H3.4A6 6 0 0 1 5 3.9zm8 0a6 6 0 0 1 1.6 1.8h-1.1c-.1-.7-.3-1.3-.5-1.8zM3 7.1h1.3v3.8H3zm2.7 0h2.6v3.8H5.7zm4 0h2.6v3.8H9.7zm4 0H15v3.8h-1.3zM3.4 12.3h1.1c.1.7.3 1.3.5 1.8a6 6 0 0 1-1.6-1.8zm2.8 0h2.1v2.6c-.9-.2-1.6-1.2-2.1-2.6zm3.5 0h2.1c-.5 1.4-1.2 2.4-2.1 2.6zm3.8 0h1.1a6 6 0 0 1-1.6 1.8c.2-.5.4-1.1.5-1.8z"/></svg>
        www.website.com
      </li>
    </ul>
  </section>
</main>
</body>
</html>
```